Harborline Motors LLC

Car Dealer Customer Service
Address: 2741 Linden Avenue, Shelbyville, TN 37162
web: www.harborlinemotorstn.net
email: harborlinemotorstn@mailbox-example.net
Phone: (931) 555-0148
Phone: (629) 555-0173

```html
<!DOCTYPE html>
<html lang="en">
<head>
<meta charset="utf-8">
<title>Harborline Motors – Business Card</title>
<link rel="stylesheet" href="https://fonts.googleapis.com/css2?family=Montserrat:ital,wght@0,700;1,400;1,800;1,900&display=swap">
<style>
  :root {
    --page: #fddd90;
    --card-edge: #ebb045;
    --card-mid: #f3c52f;
    --card-glow: #f8d91c;
    --brand-blue: #1c75ab;
    --brand-blue-light: #2a93cf;
    --white: #ffffff;
  }
  * { margin: 0; padding: 0; box-sizing: border-box; }
  html, body { width: 1064px; height: 1200px; overflow: hidden; }
  body {
    background: var(--page);
    position: relative;
    font-family: "Montserrat", sans-serif;
  }
  .card {
    position: absolute;
    width: 796px;
    height: 455px;
    overflow: hidden;
  }
  .card--front {
    left: 135px; top: 106px;
    background: radial-gradient(ellipse 60% 80% at 70% 60%, var(--card-glow) 0%, var(--card-mid) 45%, var(--card-edge) 100%);
  }
  .card--back {
    left: 134px; top: 640px;
    background: radial-gradient(ellipse 55% 65% at 50% 52%, var(--card-glow) 0%, var(--card-mid) 50%, var(--card-edge) 100%);
  }
  .brand-mark {
    position: absolute;
    border-radius: 50%;
    background: linear-gradient(180deg, var(--brand-blue-light), var(--brand-blue));
  }
  .card--front .brand-mark { left: 96px; top: 33px; width: 94px; height: 94px; }
  .card--back .brand-mark { left: 307px; top: 118px; width: 164px; height: 164px; }
  .brand-name {
    position: absolute;
    color: var(--brand-blue);
    font-weight: 700;
    white-space: nowrap;
    text-align: center;
  }
  .card--front .brand-name { left: 0; width: 286px; top: 133px; font-size: 18px; }
  .card--back .brand-name { left: 0; width: 796px; top: 296px; font-size: 38px; }

  .vehicle-photo {
    position: absolute;
    left: 86px; top: 174px;
    width: 468px; height: 218px;
    border-radius: 46% 40% 14% 14% / 40% 40% 18% 18%;
    background: radial-gradient(ellipse at 50% 45%, #f2c51a 0%, #e3b20f 55%, #9a7a18 85%, rgba(60,50,20,0.35) 100%);
  }
  .divider { position: absolute; left: 0; top: 0; }

  .headline {
    position: absolute;
    left: 398px; top: 30px;
    font-style: italic;
    font-weight: 900;
    font-size: 51px;
    line-height: 40px;
    letter-spacing: -2px;
  }
  .headline span { display: block; white-space: nowrap; }
  .headline .line-1 { color: var(--white); }
  .headline .line-2 { color: var(--white); padding-left: 22px; }
  .headline .line-3 { color: var(--brand-blue); padding-left: 45px; }

  .call {
    position: absolute;
    left: 530px; top: 248px;
  }
  .call-icon { position: absolute; left: 0; top: 0; }
  .call-label {
    position: absolute; left: 56px; top: 0;
    color: var(--brand-blue);
    font-style: italic; font-weight: 900;
    font-size: 38px; line-height: 46px;
    white-space: nowrap;
  }
  .phones {
    position: absolute;
    left: 565px; top: 294px;
    color: var(--white);
    font-style: italic; font-weight: 800;
    font-size: 27px; line-height: 36px;
    white-space: nowrap;
  }
  .footer {
    position: absolute;
    left: 42px; right: 36px; top: 406px;
    height: 34px;
    display: flex;
    align-items: center;
    justify-content: space-between;
  }
  .contact {
    color: var(--white);
    font-style: italic; font-weight: 400;
    font-size: 10.5px; line-height: 14px;
    white-space: nowrap;
    display: flex; align-items: center; gap: 6px;
    flex: none;
  }
  .contact svg { flex: none; }
</style>
</head>
<body>
  <section class="card card--front" aria-label="Business card front">
    <div class="brand-mark"></div>
    <div class="brand-name">HARBORLINE MOTORS</div>

    <div class="vehicle-photo" role="img" aria-label="Photo of a yellow sedan car, front three-quarter view"></div>

    <svg class="divider" width="796" height="455" viewBox="0 0 796 455" aria-hidden="true">
      <line x1="393" y1="36" x2="573" y2="405" stroke="#ffffff" stroke-width="3"/>
    </svg>

    <h1 class="headline">
      <span class="line-1">CAR DEALER</span>
      <span class="line-2">CUSTOMER</span>
      <span class="line-3">SERVICE</span>
    </h1>

    <div class="call">
      <svg class="call-icon" width="46" height="50" viewBox="0 0 46 50" aria-hidden="true">
        <polygon points="23,1 45,13 45,37 23,49 1,37 1,13" fill="#1c75ab"/>
        <path d="M15 14 c2-2 4-2 5 0 l2 5 c1 2 0 3-2 4 c1 3 3 6 6 8 c1-2 2-3 4-2 l5 2 c2 1 2 3 0 5 c-3 3-8 3-13-2 c-5-5-9-11-9-15 c0-2 1-4 2-5z" fill="#ffffff"/>
      </svg>
      <div class="call-label">CALL US</div>
    </div>
    <div class="phones">
      <div>(931) 555-0148</div>
      <div>(629) 555-0173</div>
    </div>

    <div class="footer">
      <div class="contact contact--address">
        <svg width="12" height="16" viewBox="0 0 12 16" aria-hidden="true">
          <path d="M6 0 C2.7 0 0 2.6 0 5.8 C0 10 6 16 6 16 S12 10 12 5.8 C12 2.6 9.3 0 6 0z M6 8.3 A2.5 2.5 0 1 1 6 3.3 A2.5 2.5 0 0 1 6 8.3z" fill="#1c75ab"/>
        </svg>
        <div>2741 LINDEN AVENUE,<br>SHELBYVILLE, TN 37162</div>
      </div>
      <div class="contact contact--email">
        <svg width="17" height="12" viewBox="0 0 17 12" aria-hidden="true">
          <rect width="17" height="12" rx="1.5" fill="#1c75ab"/>
          <path d="M1 1.5 L8.5 7 L16 1.5" fill="none" stroke="#f3c52f" stroke-width="1.3"/>
        </svg>
        <div>HARBORLINEMOTORSTN@MAILBOX-EXAMPLE.NET</div>
      </div>
      <div class="contact contact--web">
        <svg width="16" height="16" viewBox="0 0 16 16" aria-hidden="true">
          <g fill="none" stroke="#1c75ab" stroke-width="1.4">
            <circle cx="8" cy="8" r="7"/>
            <ellipse cx="8" cy="8" rx="3" ry="7"/>
            <line x1="1" y1="8" x2="15" y2="8"/>
            <line x1="2.5" y1="4.5" x2="13.5" y2="4.5"/>
            <line x1="2.5" y1="11.5" x2="13.5" y2="11.5"/>
          </g>
        </svg>
        <div>WWW.HARBORLINEMOTORSTN.NET</div>
      </div>
    </div>
  </section>

  <section class="card card--back" aria-label="Business card back">
    <div class="brand-mark"></div>
    <div class="brand-name">HARBORLINE MOTORS</div>
  </section>
</body>
</html>
```